Playbill Ad Design

Hi, I need a single page ad designed 8" tall and 5" wide at 300dpi.

Requirements
-KSV Logo
-Phone Number - 800-372-KSV4
-Web site - www.kestrelvantagestudios.example
-Email - sales@kestrelvantagestudios.example

```html
<!DOCTYPE html>
<html lang="en">
<head>
<meta charset="utf-8">
<title>KSV Playbill Ad</title>
<link rel="stylesheet" href="https://fonts.googleapis.com/css2?family=Bebas+Neue&family=Open+Sans:wght@400;600&family=Permanent+Marker&display=swap">
<style>
:root{
  --stage:#646464;
  --ink:#000;
  --white:#fff;
  --red:#e3121b;
  --red-deep:#7a0508;
  --muted:#cfcfcf;
}
*{margin:0;padding:0;box-sizing:border-box}
html,body{width:1200px;height:1137px;overflow:hidden;background:var(--stage)}
.ad{position:absolute;left:289px;top:66px;width:627px;height:1003px;background:var(--ink);overflow:hidden;color:var(--white);font-family:"Open Sans",sans-serif}
.photo{position:absolute;left:297px;top:0;width:330px;height:870px;
  background:
    radial-gradient(circle at 92% 3%,rgba(255,255,255,.85) 0,rgba(255,255,255,.25) 10%,transparent 28%),
    linear-gradient(90deg,var(--ink) 0%,rgba(0,0,0,0) 35%),
    linear-gradient(180deg,#0b0b0b 0%,#3a0507 25%,var(--red-deep) 45%,#c30f16 65%,#4a0305 85%,var(--ink) 100%)}
.brush{position:absolute;left:0;top:0;width:627px;height:1003px}
.logo{position:absolute;left:36px;top:36px;font-family:"Bebas Neue",sans-serif;font-size:72px;line-height:1;letter-spacing:2px;color:var(--white)}
.headline{position:absolute;left:42px;font-family:"Bebas Neue",sans-serif;font-size:54px;line-height:46px;color:var(--white)}
.headline.first{top:143px}
.headline.second{top:262px}
.elevate{font-family:"Permanent Marker",cursive;color:var(--red);font-size:46px;margin-left:8px;vertical-align:2px}
.intro{position:absolute;left:42px;top:388px;width:250px;font-size:16.5px;line-height:21px;color:var(--white)}
.services{position:absolute;left:36px;top:548px;list-style:none}
.service{display:flex;align-items:center;height:64px}
.service svg{width:40px;height:40px;stroke:var(--red);fill:none;stroke-width:1.6}
.service .rule{width:1px;height:46px;background:#555;margin:0 26px 0 20px}
.service span{font-size:18.5px;line-height:25px;text-transform:uppercase}
.contact{position:absolute;left:0;width:100%;top:918px;text-align:center;font-size:19.5px}
.contact .bar{display:inline-block;width:3px;height:20px;background:var(--red);margin:0 12px;vertical-align:-3px}
.site{position:absolute;left:0;width:100%;top:950px;text-align:center;font-family:"Bebas Neue",sans-serif;font-size:29px;letter-spacing:.3px}
</style>
</head>
<body>
<div class="ad">
  <div class="photo" role="img" aria-label="Photo of a red-lit event stage with LED screens, truss and a spotlight burst"></div>
  <svg class="brush" viewBox="0 0 627 1003" role="img" aria-label="Red brush stroke accent">
    <polygon points="10,905 180,850 330,800 480,760 627,718 627,805 470,835 320,870 160,900 40,915" fill="#e3121b"/>
  </svg>

  <div class="logo">KSV</div>

  <h1 class="headline first">We don’t just<br>build shows.</h1>
  <h2 class="headline second">We<span class="elevate">Elevate</span><br>Experiences!</h2>

  <p class="intro">From concept to curtain call, KSV delivers world-class staging, lighting, video, and production solutions that inspire, engage, and leave a lasting impact.</p>

  <ul class="services">
    <li class="service">
      <svg viewBox="0 0 40 40"><path d="M20 9a8 8 0 0 0-5 14v4h10v-4a8 8 0 0 0-5-14z"/><path d="M16 31h8M17 34h6M17 16l3 4 3-4M20 20v6M20 2v3M6 18H3M37 18h-3M9 7l2 2M31 7l-2 2"/></svg>
      <i class="rule"></i><span>Creative<br>Design</span>
    </li>
    <li class="service">
      <svg viewBox="0 0 40 40"><circle cx="20" cy="20" r="5"/><path d="M20 5l3 4 5-1 1 5 4 3-2 4 2 4-4 3-1 5-5-1-3 4-3-4-5 1-1-5-4-3 2-4-2-4 4-3 1-5 5 1z"/></svg>
      <i class="rule"></i><span>Production<br>Solutions</span>
    </li>
    <li class="service">
      <svg viewBox="0 0 40 40"><rect x="4" y="7" width="32" height="22"/><path d="M17 13v10l8-5zM15 34h10M20 29v5"/></svg>
      <i class="rule"></i><span>Video &amp; LED<br>Technology</span>
    </li>
    <li class="service">
      <svg viewBox="0 0 40 40"><path d="M3 8h34M3 12h34M6 12v24M34 12v24M6 20l28 0M6 12l8 8M34 12l-8 8M14 20c0 6 12 6 12 0M3 36h34"/></svg>
      <i class="rule"></i><span>Staging &amp;<br>Rigging</span>
    </li>
  </ul>

  <p class="contact">(800) 372-KSV4<i class="bar"></i>sales@kestrelvantagestudios.example</p>
  <p class="site">KESTRELVANTAGESTUDIOS.EXAMPLE</p>
</div>
</body>
</html>
```